Indonesian B2B Company (Varo Ingredients) - Stationery Design

Varo Ingredients needs a corporate, bold and professional-looking stationery design.

Varo Ingredients is a new Indonesian company manufacturing, marketing and distributing various ingredients / raw materials such as flavours, fragrance, colours, sweeteners, preservatives for the food & beverage, pharmaceutical, personal care and other household goods industries.

It is a business to business (B2B) company as we supply various natural and synthetic raw materials to various consumer goods manufacturers. We therefore need a logo/identity with corporate and industrial style.

Varo Ingredients is a startup company which belongs to a larger Varo Tunggal group of companies (http://varotunggal.dealpathway.com/about) that focuses in the mining, petroleum and energy businesses. Varo Ingredients would like to focus in providing good quality, safe, reliable and affordable ingredients for the industries. Our tagline is "Ingredients for Your Success"
Updates

We have updated some information including our requirements and contact details to be shown in the stationery. Please check the project brief.

Regards,

Varo Ingredients

Target Market(s)

Manufacturers of food & beverages, personal care, pharmaceutical and other FMCG factories.

Industry/Entity Type

Business

Requirements
Must have
• Smart, professional and corporate touches in the stationery designs. We require designs for:
1. Letterhead
2. Envelope (with and without window)
3. Name card
4. Powerpoint presentation template
5. CD label
6. Small memo / with compliments card

Contact details:

Company name:
PT Varo Ingredients

Address:
Ruko Melati Sentosa Utara, Blok K07 no: 15-16
Duren Sawit Selatan, 13470
Indonesia

Tel:+62 21 738 2906
Fax:+62 21 738 2907
Email: info@varo-ingredients.co.id
Website: www.varo-ingredients.co.id

```html
<!DOCTYPE html>
<html lang="en">
<head>
<meta charset="utf-8">
<title>Varo Ingredients – Letterhead</title>
<link href="https://fonts.googleapis.com/css2?family=Source+Sans+3:wght@400&display=swap" rel="stylesheet">
<style>
  :root {
    --brand-red: #d7262f;
    --brand-yellow: #f7a823;
    --brand-blue: #1b75bc;
    --ink: #1a1a1a;
    --muted: #9a9a9a;
    --paper: #ffffff;
  }
  html, body {
    margin: 0;
    padding: 0;
    width: 828px;
    height: 1200px;
    overflow: hidden;
    background: var(--paper);
  }
  .letterhead {
    position: relative;
    width: 828px;
    height: 1200px;
    background: var(--paper);
    font-family: "Source Sans 3", Arial, sans-serif;
    color: var(--ink);
  }
  .brand {
    position: absolute;
    left: 68px;
    top: 128px;
  }
  .brand__name {
    margin: 0;
    font-size: 26px;
    font-weight: 400;
    color: var(--ink);
    line-height: 1;
  }
  .brand__line {
    margin: 7px 0 0 3px;
    font-size: 13px;
    font-weight: 400;
    color: var(--muted);
    line-height: 1;
  }
  .stripes {
    position: absolute;
    display: flex;
  }
  .stripes span { width: 10px; height: 100%; }
  .stripes--top-right { right: 0; top: 0; height: 527px; }
  .stripes--bottom-left { left: 0; top: 528px; height: 672px; }
  .stripe--red { background: var(--brand-red); }
  .stripe--yellow { background: var(--brand-yellow); }
  .stripe--blue { background: var(--brand-blue); }
  .contact {
    position: absolute;
    top: 1108px;
    margin: 0;
    font-size: 14.5px;
    line-height: 17px;
    font-style: normal;
  }
  .contact--address { left: 78px; }
  .contact--channels { left: 558px; }
</style>
</head>
<body>
  <main class="letterhead">
    <header class="brand">
      <p class="brand__name">Varo Ingredients</p>
      <p class="brand__line">Raw Materials for Industry</p>
    </header>

    <div class="stripes stripes--top-right" aria-hidden="true">
      <span class="stripe--blue"></span>
      <span class="stripe--yellow"></span>
      <span class="stripe--red"></span>
    </div>
    <div class="stripes stripes--bottom-left" aria-hidden="true">
      <span class="stripe--red"></span>
      <span class="stripe--yellow"></span>
      <span class="stripe--blue"></span>
    </div>

    <address class="contact contact--address">
      Ruko Melati Sentosa Utara, Blok K07 no: 15-16<br>
      Duren Sawit Selatan, 13470<br>
      Indonesia.
    </address>
    <address class="contact contact--channels">
      Tel:+62 21 738 2906<br>
      Fax:+62 21 738 2907<br>
      Website: www.varo-ingredients.co.id<br>
      Email: info@varo-ingredients.co.id
    </address>
  </main>
</body>
</html>
```